Thornvale plumbing business cards

Want a functional designed for my business cards using my logo

Company Name- Thornvale Plumbing, Heating & Water Systems
Name- Martin Thornvale
Title- Vice President
Cell- 555-318-7742
Email- Thornvaleplumbing@mailbrook.example
Business address-
PO Box 57
Alderbrook, NE 21990

Plumbing

```html
<!DOCTYPE html>
<html lang="en">
<head>
<meta charset="utf-8">
<title>Thornvale Plumbing – Business Cards</title>
<link href="https://fonts.googleapis.com/css2?family=Roboto:wght@400;500&display=swap" rel="stylesheet">
<style>
  :root {
    --page-bg: #6e5140;
    --card-dark: #1c1d1f;
    --brand-blue: #0a6ebd;
    --brand-blue-deep: #1268b0;
    --band-light: #a9c3ea;
    --text-light: #e6e6e6;
    --text-muted: #b9bcc2;
    --title-grey: #8e9aab;
    --divider: #5a5c60;
    --white: #ffffff;
  }
  * { box-sizing: border-box; margin: 0; padding: 0; }
  html, body {
    width: 1125px;
    height: 1200px;
    overflow: hidden;
    background: var(--page-bg);
    font-family: "Roboto", Arial, sans-serif;
  }
  .canvas { position: relative; width: 1125px; height: 1200px; }

  .card {
    position: absolute;
    left: 150px;
    width: 825px;
    height: 470px;
    box-shadow: 0 6px 16px rgba(0,0,0,0.35);
    overflow: hidden;
  }

  /* Front */
  .card-front { top: 98px; background: var(--card-dark); }
  .brand {
    position: absolute;
    right: 48px;
    top: 134px;
    width: 300px;
    display: flex;
    align-items: center;
    justify-content: center;
    gap: 10px;
  }
  .brand-mark { flex: 0 0 14px; width: 14px; height: 14px; background: var(--brand-blue); }
  .brand-name {
    font-size: 30px;
    font-weight: 400;
    color: var(--brand-blue);
    white-space: nowrap;
  }
  .office-phone {
    position: absolute;
    right: 48px;
    top: 212px;
    width: 300px;
    text-align: center;
    font-size: 29px;
    color: var(--brand-blue);
  }
  .person { position: absolute; left: 48px; top: 276px; }
  .person-name { font-size: 30px; font-weight: 500; color: var(--brand-blue-deep); line-height: 1.1; }
  .person-title { font-size: 20px; font-weight: 500; color: var(--title-grey); margin-top: 2px; }
  .divider {
    position: absolute;
    left: 48px; right: 48px; top: 352px;
    height: 2px; background: var(--divider);
  }
  .contact { position: absolute; left: 48px; top: 370px; list-style: none; }
  .contact li {
    display: flex; align-items: center; gap: 12px;
    font-size: 19px; color: var(--text-muted); height: 26px;
  }
  .contact svg { flex: 0 0 16px; width: 16px; height: 16px; fill: var(--brand-blue); }
  .address {
    position: absolute; right: 48px; top: 370px;
    text-align: right; font-size: 19px; line-height: 26px;
    color: var(--text-light); font-style: normal;
  }
  .accent-band { position: absolute; left: 0; bottom: 0; width: 100%; height: 16px; }

  /* Back */
  .card-back { top: 631px; background: var(--brand-blue); }
  .back-brand {
    position: absolute; right: 58px; top: 318px; width: 300px;
    text-align: center; font-size: 30px; color: var(--white);
  }
  .website {
    position: absolute; right: 58px; top: 392px; width: 300px;
    text-align: center; font-size: 19px; color: #e8f1fa;
  }
</style>
</head>
<body>
<div class="canvas">
  <section class="card card-front" aria-label="Business card front">
    <div class="brand">
      <span class="brand-mark"></span>
      <span class="brand-name">Thornvale Plumbing</span>
    </div>
    <div class="office-phone">555.204.6613</div>

    <div class="person">
      <div class="person-name">Martin Thornvale</div>
      <div class="person-title">Vice President</div>
    </div>

    <div class="divider"></div>

    <ul class="contact">
      <li>
        <svg viewBox="0 0 24 24" aria-hidden="true"><path d="M6.6 10.8a15.2 15.2 0 0 0 6.6 6.6l2.2-2.2a1 1 0 0 1 1-.25 11.4 11.4 0 0 0 3.6.57 1 1 0 0 1 1 1V20a1 1 0 0 1-1 1A17 17 0 0 1 3 4a1 1 0 0 1 1-1h3.5a1 1 0 0 1 1 1c0 1.25.2 2.45.57 3.57a1 1 0 0 1-.25 1z"/></svg>
        555-318-7742
      </li>
      <li>
        <svg viewBox="0 0 24 24" aria-hidden="true"><path d="M2 5h20v14H2z"/><path d="M3 6l9 6.3L21 6" stroke="#1c1d1f" stroke-width="1.6" fill="none"/></svg>
        Thornvaleplumbing@mailbrook.example
      </li>
    </ul>

    <address class="address">PO Box 57<br>Alderbrook, NE 21990</address>

    <svg class="accent-band" viewBox="0 0 825 16" preserveAspectRatio="none" aria-hidden="true">
      <polygon points="0,0 492,0 487,16 0,16" fill="var(--brand-blue)"/>
      <polygon points="495,0 825,0 825,16 490,16" fill="var(--band-light)"/>
    </svg>
  </section>

  <section class="card card-back" aria-label="Business card back">
    <div class="back-brand">Thornvale Plumbing</div>
    <div class="website">www.Thornvaleplumbing.example</div>
  </section>
</div>
</body>
</html>
```